Elegant Black Candle Label Design!

I need a 2.375" tall by 3.0" wide candle label design. I'm looking for simple and elegant. Black label with silver leaf border and lettering. Label needs to have the following information on it: Fern Hollow Candle Co. as the company name, scent name in the middle and in smaller font, it needs to say Made in USA, All Natural, 8oz. Attached photos are for inspiration.

Target Market(s)

People looking for high end, all natural candle fragrances

Industry/Entity Type

Candle-Spa

Colors

Designer to choose only greyscale colors for use in the design.

Requirements
Must have
• Company Name, Scent (ability to change scent names), All Natural, Made in USA, 8oz
Nice to have
• Black background, silver leaf border and silver leaf font. Elegant fonts maybe slightly cursive

```html
<!DOCTYPE html>
<html lang="en">
<head>
<meta charset="utf-8">
<title>Fern Hollow Candle Co. — Label</title>
<link href="https://fonts.googleapis.com/css2?family=Great+Vibes&family=Montserrat:wght@400;500&display=swap" rel="stylesheet">
<style>
  :root {
    --backdrop: #3b3b3b;
    --label-black: #050505;
    --silver: #d2d2d2;
    --silver-soft: #a9a9a9;
    --white: #f4f4f4;
  }
  * { margin: 0; padding: 0; box-sizing: border-box; }
  html, body {
    width: 1200px;
    height: 900px;
    overflow: hidden;
    background: var(--backdrop);
  }
  .canvas {
    position: relative;
    width: 1200px;
    height: 900px;
  }
  .label {
    position: absolute;
    left: 120px;
    top: 71px;
    width: 960px;
    height: 758px;
    background: var(--label-black);
    overflow: hidden;
  }
  .label-art {
    position: absolute;
    inset: 0;
  }
  .label-text {
    position: absolute;
    left: 0;
    width: 100%;
    text-align: center;
    white-space: nowrap;
  }
  .brand-name {
    top: 128px;
    font-family: "Great Vibes", cursive;
    font-size: 112px;
    line-height: 1;
    color: var(--silver);
  }
  .brand-tagline {
    top: 236px;
    font-family: "Montserrat", sans-serif;
    font-weight: 500;
    font-size: 29px;
    letter-spacing: 0.28em;
    padding-left: 0.28em;
    color: var(--silver-soft);
  }
  .scent-name {
    top: 392px;
    font-family: "Montserrat", sans-serif;
    font-weight: 400;
    font-size: 50px;
    letter-spacing: 0.1em;
    padding-left: 0.1em;
    color: var(--white);
  }
  .origin {
    top: 552px;
    font-family: "Montserrat", sans-serif;
    font-weight: 500;
    font-size: 15px;
    letter-spacing: 0.04em;
    color: var(--white);
  }
  .details {
    top: 612px;
    font-family: "Montserrat", sans-serif;
    font-weight: 500;
    font-size: 25px;
    line-height: 34px;
    letter-spacing: 0.03em;
    color: var(--white);
  }
</style>
</head>
<body>
<main class="canvas">
  <section class="label">
    <svg class="label-art" width="960" height="758" viewBox="0 0 960 758" aria-hidden="false">
      <defs>
        <linearGradient id="foliage-silver" x1="0" y1="0" x2="1" y2="1">
          <stop offset="0" stop-color="#e6e6e6" stop-opacity="0.55"/>
          <stop offset="0.6" stop-color="#9a9a9a" stop-opacity="0.3"/>
          <stop offset="1" stop-color="#5a5a5a" stop-opacity="0"/>
        </linearGradient>
        <linearGradient id="foliage-silver-br" x1="1" y1="1" x2="0" y2="0">
          <stop offset="0" stop-color="#e6e6e6" stop-opacity="0.55"/>
          <stop offset="0.6" stop-color="#9a9a9a" stop-opacity="0.3"/>
          <stop offset="1" stop-color="#5a5a5a" stop-opacity="0"/>
        </linearGradient>
      </defs>

      <g class="frame" fill="none" stroke="var(--silver)" stroke-width="3">
        <polyline points="330,43 917,43 917,358"/>
        <polyline points="43,380 43,715 650,715"/>
      </g>

      <path class="foliage foliage-top-left" role="img" aria-label="Silver leaf sprigs in the top left corner"
            d="M0,0 L352,0 C300,40 200,110 150,200 C110,270 70,330 40,369 L0,369 Z"
            fill="url(#foliage-silver)"/>
      <path class="foliage foliage-bottom-right" role="img" aria-label="Silver leaf sprigs in the bottom right corner"
            d="M960,326 L960,758 L650,758 C700,720 790,690 840,620 C880,560 900,440 930,326 Z"
            fill="url(#foliage-silver-br)"/>
    </svg>

    <h1 class="label-text brand-name">Fern Hollow</h1>
    <p class="label-text brand-tagline">CANDLE CO.</p>
    <h2 class="label-text scent-name">SCENT NAME</h2>
    <p class="label-text origin">MADE IN USA</p>
    <p class="label-text details">ALL NATURAL<br>8oz.</p>
  </section>
</main>
</body>
</html>
```